Handout for attendees of educational seminar

I provide educational workshops on how to give technical presentations at conferences to scientists and engineers. My company is called Craft Talk Studio (www.CraftTalkStudio.example). I would like a double sided, half page size flyer that can be used as a handout for attendees of my workshops. On one side of the flyer, they will get top tips for creating their next presentation. On the other side, they will get my photo, bio, and contact information. I have uploaded a draft of a full page design I made myself. I'd like the copy of the tips to remain the same, but everything else is flexible.

Target Market(s)

scientists, engineers, technical professionals

Font styles to use
Serif
Sans Serif

Requirements
Must have
• my photo (I've provided two options to choose from depending on colors...photo on side 2 only), my logo, flyer needs to be half page in size (5.5" x 8.5"), needs to be double sided, One side has the "tips" and the other side has my personal details (see attached page for copy).
Nice to have
• I like the use of icons on the "tips" side of the flyer.

```html
<!DOCTYPE html>
<html lang="en">
<head>
<meta charset="utf-8">
<title>Meet Dana – Craft Talk Studio</title>
<link rel="stylesheet" href="https://fonts.googleapis.com/css2?family=Abril+Fatface&family=Arimo:wght@400&family=Raleway:wght@500&display=swap">
<style>
  :root {
    --sky-light: #b9e1fb;
    --sky: #93cdf3;
    --sky-deep: #7fc2ee;
    --navy: #1c2a52;
    --ink: #15181f;
    --frame: #ffffff;
    --photo-warm: #c9a58c;
    --photo-green: #1f8a5a;
    --logo-grey: #4a4a4a;
    --brand-green: #9bb53e;
  }
  * { box-sizing: border-box; margin: 0; padding: 0; }
  html, body { width: 776px; height: 1200px; overflow: hidden; }
  body {
    background: linear-gradient(160deg, var(--sky-light) 0%, var(--sky) 55%, var(--sky-deep) 100%);
    font-family: "Arimo", Arial, sans-serif;
    color: var(--ink);
    position: relative;
  }
  .portrait-frame {
    position: absolute;
    left: 100px; top: 37px;
    width: 587px; height: 387px;
    background: var(--frame);
    border-radius: 16px;
    padding: 19px 20px 17px 20px;
  }
  .portrait {
    width: 100%; height: 100%;
    background: linear-gradient(180deg, #d9c8b6 0%, var(--photo-warm) 45%, var(--photo-green) 100%);
  }
  .bio-title {
    position: absolute;
    top: 444px; left: 0; width: 100%;
    text-align: center;
    font-family: "Abril Fatface", Georgia, serif;
    font-weight: 400;
    font-size: 33px;
    color: var(--navy);
  }
  .bio {
    position: absolute;
    left: 51px; top: 494px; width: 690px;
    font-size: 20.3px;
    line-height: 28px;
  }
  .bio p + p { margin-top: 28px; }
  .brand {
    position: absolute;
    top: 977px; left: 0; width: 100%;
    text-align: center;
    color: var(--brand-green);
    font-family: "Raleway", Arial, sans-serif;
    font-weight: 500;
  }
  .brand-dot {
    display: block;
    width: 98px; height: 98px;
    margin: 0 auto 6px;
    border-radius: 50%;
    background: var(--logo-grey);
  }
  .brand-name { font-size: 29px; line-height: 32px; display: block; }
  .brand-line { font-size: 14px; letter-spacing: 2px; display: block; }
  .contact {
    position: absolute;
    top: 1141px; left: 51px; width: 690px;
    display: flex; justify-content: space-between;
    font-size: 20.3px;
  }
</style>
</head>
<body>
  <div class="portrait-frame">
    <div class="portrait" role="img" aria-label="Portrait photo of Dana Whitfield in a green top"></div>
  </div>

  <h1 class="bio-title">Meet Dana</h1>

  <div class="bio">
    <p>Dana Whitfield is on a mission: to transform how scientists, engineers, and technical professionals present their work. That’s because she believes that even the best technical ideas are destined to remain undiscovered unless presented in a clear and compelling way that sparks innovation and drives adoption.</p>
    <p>For a decade, she’s traveled around the world to work with Top 100 corporations, institutions and universities, teaching the proven strategies she’s mastered through her consulting work and during her time as a faculty member Lakeshore State University.</p>
    <p>Dana is internationally known for her popular StageIdeas Talk entitled "Speak Geek to Me" which has over 2 million views (and counting!). Teams that work with Dana get the practical skills and natural confidence they need to immediately shift their “information dump” -style presentations into ones that are meaningful, engaging, and inspire people to take action. Dana provides on-site group workshops and coaching, conference sessions and keynotes, and 1:1 consultation.</p>
  </div>

  <div class="brand">
    <span class="brand-dot"></span>
    <span class="brand-name">Dana Whitfield</span>
    <span class="brand-line">Craft Talk Studio</span>
  </div>

  <div class="contact">
    <span class="contact-web">www.CraftTalkStudio.example</span>
    <span class="contact-email">dana@crafttalkstudio.example</span>
  </div>
</body>
</html>
```